New name flyer

We have just changed our business name from kR Property group to Harbour Lantern. We want to distribute a flyer to the local community to inform them of the change. We are a realestate agency which focuses mainly on property management but also sales. We service from Brisbane to the Sunshine coast.

Target Market(s)

Local community

Industry/Entity Type

realestate

Requirements
Must have
• Details of name change
Nice to have
• Servicing area Brisbane and Sunshine Coast, no change in management or services we offer, and will continue pride ourselves on offering a high level of service, with the same team from the Gold to Sunshine Coast.
Should not have
• too much wording.

```html
<!DOCTYPE html>
<html lang="en">
<head>
<meta charset="utf-8">
<title>Harbour Lantern – New Name Flyer</title>
<link rel="stylesheet" href="https://fonts.googleapis.com/css2?family=Barlow+Condensed:wght@300;600;700;800&family=Barlow:wght@300;700&display=swap">
<style>
  :root {
    --blue-light: #5ba6fa;
    --blue-mid: #3a86e2;
    --blue-deep: #0c52b0;
    --ink-blue: #0d57b5;
    --white: #ffffff;
    --grey-text: #7a7a7a;
    --body-ink: #1d1d1d;
    --horn-light: #f7f7f7;
    --horn-shade: #c9ced3;
  }
  html, body { margin: 0; padding: 0; overflow: hidden; }
  body { width: 1200px; height: 1200px; }
  .flyer {
    position: relative;
    width: 1200px;
    height: 1200px;
    overflow: hidden;
    background:
      radial-gradient(circle at 600px 440px, var(--blue-light) 0%, var(--blue-mid) 40%, var(--blue-deep) 100%);
    font-family: "Barlow", sans-serif;
    color: var(--white);
  }
  .brand {
    position: absolute;
    left: 75px;
    top: 140px;
    margin: 0;
    font-family: "Barlow", sans-serif;
    font-weight: 700;
    font-size: 34px;
    line-height: 1.05;
    letter-spacing: 2px;
    text-transform: uppercase;
    color: var(--white);
  }
  .hero-art {
    position: absolute;
    left: 296px;
    top: 60px;
    width: 610px;
    height: 460px;
    border-radius: 48% 52% 46% 54% / 50% 50% 50% 50%;
    background: radial-gradient(ellipse at 70% 40%, var(--horn-light) 0%, #e4e7ea 45%, var(--horn-shade) 75%, rgba(201,206,211,0) 100%);
    opacity: 0.9;
  }
  .headline {
    position: absolute;
    left: 0;
    top: 0;
    width: 1200px;
    height: 1200px;
  }
  .headline .band { fill: var(--white); }
  .headline .important {
    font-family: "Barlow Condensed", sans-serif;
    font-weight: 800;
    font-size: 168px;
    fill: var(--ink-blue);
  }
  .headline .announcement {
    font-family: "Barlow Condensed", sans-serif;
    font-weight: 800;
    font-size: 116px;
    fill: var(--white);
  }
  .intro {
    position: absolute;
    left: 0;
    top: 878px;
    width: 1200px;
    margin: 0;
    text-align: center;
    font-family: "Barlow Condensed", sans-serif;
    font-weight: 300;
    font-size: 50px;
    letter-spacing: -0.5px;
  }
  .name-change {
    position: absolute;
    left: 142px;
    top: 948px;
    width: 914px;
    height: 78px;
  }
  .name-box {
    position: absolute;
    top: 9px;
    width: 374px;
    height: 60px;
    background: var(--white);
    display: flex;
    align-items: center;
    justify-content: center;
    font-family: "Barlow Condensed", sans-serif;
    font-weight: 700;
    font-size: 46px;
  }
  .name-box.old { left: 0; color: var(--grey-text); }
  .name-box.new { left: 540px; color: var(--ink-blue); }
  .name-arrow { position: absolute; left: 388px; top: 0; }
  .note {
    position: absolute;
    left: 75px;
    top: 1060px;
    width: 1050px;
    height: 92px;
    box-sizing: border-box;
    border-radius: 18px;
    background: var(--white);
    color: var(--body-ink);
    display: flex;
    align-items: center;
    justify-content: center;
    text-align: center;
    margin: 0;
    padding: 0 20px;
    font-family: "Barlow", sans-serif;
    font-weight: 300;
    font-size: 20px;
    line-height: 1.45;
  }
</style>
</head>
<body>
  <main class="flyer">
    <p class="brand">Harbour<br>Lantern</p>

    <div class="hero-art" role="img" aria-label="Illustration of a white megaphone with a grey handle, sound bolts flying to the right"></div>

    <svg class="headline" viewBox="0 0 1200 1200" aria-label="Important announcement">
      <g transform="translate(233,573) skewY(-9.3)">
        <rect class="band" x="0" y="0" width="734" height="163"/>
        <text class="important" x="38" y="148" textLength="662" lengthAdjust="spacingAndGlyphs">IMPORTANT</text>
        <text class="announcement" x="17" y="255" textLength="700" lengthAdjust="spacingAndGlyphs">ANNOUNCEMENT</text>
      </g>
    </svg>

    <p class="intro">We have just changed our business name from</p>

    <div class="name-change">
      <div class="name-box old">kR Property group</div>
      <svg class="name-arrow" width="142" height="78" viewBox="0 0 142 78" aria-hidden="true">
        <polygon points="0,24 73,24 73,0 140,39 73,78 73,54 0,54" fill="#ffffff"/>
      </svg>
      <div class="name-box new">Harbour Lantern</div>
    </div>

    <p class="note">Servicing area Brisbane and Sunshine Coast, no change in management or services we offer, and will continue<br>pride ourselves on offering a high level of service, with the same team from the Gold to Sunshine Coast.</p>
  </main>
</body>
</html>
```